New Business Card Design Project

I need a meaningful new business card. Therefore, the website should convey growth, joy, uniqueness, workout and a bit of luxury.
Color scheme should be petrol, gold and matching colors.

```html
<!DOCTYPE html>
<html lang="de">
<head>
<meta charset="utf-8">
<title>Corevia Pilates – Visitenkarte</title>
<link rel="stylesheet" href="https://fonts.googleapis.com/css2?family=Montserrat:wght@400;500;700&display=swap">
<style>
  :root{
    --stage:#1d1d1d;
    --paper:#f4f4f4;
    --ink:#3a3a3a;
    --petrol:#18a39a;
    --slate:#4a4a4c;
    --night:#2a2a2c;
    --mist:#e8e8e8;
  }
  *{margin:0;padding:0;box-sizing:border-box}
  html,body{width:1200px;height:1059px;overflow:hidden;background:var(--stage);font-family:"Montserrat",sans-serif}
  .canvas{position:relative;width:1200px;height:1059px}
  .card{position:absolute;border-radius:24px;overflow:hidden}
  .card--front{left:257px;top:89px;width:687px;height:390px;background:var(--paper)}
  .card--back{left:254px;top:547px;width:693px;height:393px;background:var(--night)}

  .brand{position:absolute;display:flex;flex-direction:column;align-items:center;justify-content:center;color:var(--petrol);font-weight:500;text-align:center;line-height:1.15}
  .brand__dot{width:14px;height:14px;border-radius:50%;background:var(--petrol);margin-bottom:10px}
  .card--front .brand{left:149px;top:111px;width:147px;height:167px;font-size:22px}
  .card--back .brand{left:0;top:0;width:100%;height:100%;font-size:44px}
  .card--back .brand__dot{width:22px;height:22px;margin-bottom:18px}

  .divider{position:absolute;left:322px;top:112px;width:1px;height:165px;background:var(--ink)}
  .identity{position:absolute;left:349px;top:109px}
  .identity__name{color:var(--petrol);font-weight:700;font-size:22.5px;letter-spacing:.5px;line-height:1}
  .identity__role{color:var(--ink);font-size:16.5px;margin-top:6px}
  .contacts{list-style:none;position:absolute;left:347px;top:183px;color:var(--ink);font-size:16.5px}
  .contacts li{display:flex;align-items:center;height:25.3px}
  .contacts svg{width:11px;height:11px;margin-right:6px;fill:var(--petrol);flex:none}
  .contacts .accent{color:var(--petrol)}

  .band{position:absolute;left:0;bottom:0;width:100%;height:13px}
</style>
</head>
<body>
<main class="canvas">
  <section class="card card--front">
    <div class="brand"><span class="brand__dot"></span>Corevia<br>Pilates</div>
    <div class="divider"></div>
    <div class="identity">
      <h1 class="identity__name">LENA MARQUARDT</h1>
      <p class="identity__role">Pilates Studio Trainerin</p>
    </div>
    <ul class="contacts">
      <li><svg viewBox="0 0 12 12"><path d="M2.5 1l2 2.2-1 1.3c.6 1.5 2 2.9 3.5 3.5l1.3-1 2.2 2-1.3 1.6C4.8 10.3 1.7 7.2 1 2.3z"/></svg>+49 151 2046318</li>
      <li><svg viewBox="0 0 12 12"><path d="M0 2h12v8H0zM1 3l5 3.5L11 3v-.2H1z" fill-rule="evenodd"/></svg>info@corevia-studio.de</li>
      <li><svg viewBox="0 0 12 12"><circle cx="6" cy="6" r="5.5"/></svg>www.<span class="accent">Corevia-studio</span>.de</li>
      <li><svg viewBox="0 0 12 12"><path d="M3 .5h6A2.5 2.5 0 0 1 11.5 3v6A2.5 2.5 0 0 1 9 11.5H3A2.5 2.5 0 0 1 .5 9V3A2.5 2.5 0 0 1 3 .5zm0 1.3A1.2 1.2 0 0 0 1.8 3v6A1.2 1.2 0 0 0 3 10.2h6A1.2 1.2 0 0 0 10.2 9V3A1.2 1.2 0 0 0 9 1.8zM6 3.4A2.6 2.6 0 1 1 6 8.6 2.6 2.6 0 0 1 6 3.4zm0 1.2a1.4 1.4 0 1 0 0 2.8 1.4 1.4 0 0 0 0-2.8z" fill-rule="evenodd"/></svg>corevia_pilatesstudio</li>
    </ul>
    <svg class="band" viewBox="0 0 687 13" preserveAspectRatio="none">
      <polygon points="0,0 352,0 326,13 0,13" fill="var(--petrol)"/>
      <polygon points="358,0 687,0 687,13 338,13" fill="var(--slate)"/>
    </svg>
  </section>

  <section class="card card--back">
    <div class="brand"><span class="brand__dot"></span>Corevia<br>Pilates</div>
  </section>
</main>
</body>
</html>
```